App UI Design: Shopping/E-commerce App

Project :
Develop an UI design & App icon for an E-commerce/Shopping App

About the App/ Target Audience:
This grocery & food shopping app will be used by independent pub, café, restaurant owners to place & manage their purchases of foods and groceries for their catering businesses.

They will use the app to access product catalogues & special promotions, search & buy large quantities of groceries or catering supplies, and the ability to manage and track status of their order.

The HTML5 App’s has been built with a very basic structure. It now needs the visual layer of the UI designed

Note:
The app is tailored for business & catering orders, not retail/supermarket buyers, so the visual needs to look smart & not too casual.
Updates

Reason: Current submissions have not met out expectations. Please use the similar app examples in the PDF as a strong point of reference for the look & feel. Feedback will be given as submissions come in, please feel free to submit initial concepts of 1 or 2 of the pages & we'll provide feedback on whether it is on the right track or not before you do more work. Current submission will also receive feedback in the next few days. We look forward to new submissions!

Target Market(s)

Male & Female. Independent pub, café, restaurant owners buying for their catering businesses. Chefs etc.

Industry/Entity Type

Restaurant

Requirements
Must have
• An overview of elements/pages of the app that needs to be designed are:
(DOWNLOAD a more detailed diagram PDF explanation)

1. Welcome- Log-in Page
2. Homepage – index that links to different function of the app

Products:
3. Promotions page – for products on special for a limited time
4. Catalogue page – access to a range of catalogue

Ways to buy:
5. Basket (Shopping Cart) - tracking items they are buying from the catalogues
6. Templates (Pre-set Shopping list)- Set shopping list that has been preloaded for certain menu
7. Open Order page

My Account:
8. My Account/profile page – Users can check the status of their order, look at past orders, look at their account number & details etc

_______________________________________________________

Icon set- Icons to represent each pages that act as visual cues for easier browsing.

2 Main features that need to be accessible & consistent throughout all pages are:
a) The Navigation Bar –
so the user can quickly find their way back & access to the main functions
b) The Search bar –
whether it drops down when needed, or is featured as a header/footer.
c) Log out button
Nice to have

Things to keep in mind:

The UI design essentially needs to be a customizable template that can easily adapt to any brand/logo with a slight change of the color scheme. As we will later implement our brand & logo onto it.

We’re looking for a clean & clear design that allows for a straight forward easy user experience.

You are free to develop different layout & UI pattern that you feel is the most efficient way the user can walk through the App & make their purchase in no more than 2 or 3 clicks
________________________________________________

Screenshot of Similar Apps for reference are also in the PDF

```html
<!DOCTYPE html>
<html lang="en">
<head>
<meta charset="utf-8">
<title>Home – Catering Orders</title>
<link href="https://fonts.googleapis.com/css2?family=Arimo:wght@400;700&display=swap" rel="stylesheet">
<style>
  :root {
    --status-black: #000000;
    --sky-light: #5fdcf8;
    --sky-mid: #47d0f3;
    --sky-deep: #2cc2ee;
    --edge-blue: #1ea7dc;
    --button-top: #2cc0f6;
    --button-bottom: #0a8ee2;
    --white: #ffffff;
    --placeholder: #a9a9a9;
    --field-border: #9fc9da;
    --panel-shadow: rgba(0, 0, 0, 0.28);
  }
  * { box-sizing: border-box; margin: 0; padding: 0; }
  html, body { width: 800px; height: 1200px; overflow: hidden; background: var(--white); }
  body { font-family: "Arimo", Helvetica, Arial, sans-serif; position: relative; }

  .status-bar {
    position: absolute; left: 0; top: 0; width: 800px; height: 50px;
    background: var(--status-black); color: var(--white);
    font-weight: 700; font-size: 28px;
  }
  .status-bar .signal { position: absolute; left: 10px; top: 14px; }
  .status-bar .carrier { position: absolute; left: 58px; top: 9px; }
  .status-bar .clock { position: absolute; left: 0; right: 0; top: 9px; text-align: center; }
  .status-bar .alarm { position: absolute; left: 695px; top: 12px; }
  .status-bar .battery { position: absolute; left: 738px; top: 13px; }

  .nav-bar {
    position: absolute; left: 0; top: 50px; width: 800px; height: 110px;
    background: linear-gradient(180deg, var(--sky-light), var(--sky-mid));
    border-bottom: 2px solid var(--edge-blue);
  }
  .nav-title {
    position: absolute; left: 0; right: 0; top: 22px; text-align: center;
    color: var(--white); font-weight: 700; font-size: 46px;
    text-shadow: 0 -1px 1px rgba(0,0,0,0.15);
  }
  .sign-out {
    position: absolute; left: 637px; top: 17px; width: 151px; height: 73px;
    border-radius: 10px; border: 2px solid #33c8f5;
    background: linear-gradient(180deg, var(--button-top), var(--button-bottom));
    color: var(--white); font-weight: 700; font-size: 28px;
    display: flex; align-items: center; justify-content: center;
    box-shadow: 0 1px 2px rgba(0,0,0,0.25);
  }

  .search-band {
    position: absolute; left: 0; top: 160px; width: 800px; height: 109px;
    background: linear-gradient(180deg, var(--sky-mid), var(--sky-deep));
    border-bottom: 2px solid var(--edge-blue);
  }
  .search-field {
    position: absolute; left: 13px; top: 20px; width: 774px; height: 70px;
    border-radius: 35px; background: var(--white);
    border: 2px solid var(--field-border);
    box-shadow: inset 0 3px 5px rgba(0,0,0,0.25);
    display: flex; align-items: center; padding-left: 22px;
  }
  .search-field .placeholder {
    margin-left: 16px; color: var(--placeholder); font-weight: 700; font-size: 33px;
  }

  .home-grid {
    position: absolute; left: 100px; top: 332px; width: 600px; height: 648px;
    border-radius: 10px; border: 2px solid var(--edge-blue);
    background: linear-gradient(90deg, var(--sky-deep), var(--sky-light) 45%, var(--sky-light) 55%, var(--sky-deep));
    box-shadow: 0 22px 14px -10px var(--panel-shadow);
  }
  .divider { position: absolute; background: rgba(255,255,255,0.55); box-shadow: 1px 1px 0 var(--edge-blue); }
  .divider.vertical { left: 299px; top: 12px; width: 3px; height: 624px; }
  .divider.row-one { left: 28px; top: 212px; width: 550px; height: 3px; }
  .divider.row-two { left: 28px; top: 437px; width: 550px; height: 3px; }

  .tile-icon { position: absolute; }
  .tile-label {
    position: absolute; width: 300px; text-align: center;
    color: var(--white); font-weight: 700; font-size: 26px;
    text-shadow: 0 1px 1px rgba(0,0,0,0.12);
  }
  .col-left { left: 21px; }
  .col-right { left: 293px; }
</style>
</head>
<body>

<header class="status-bar">
  <svg class="signal" width="42" height="20" viewBox="0 0 42 20" fill="#fff">
    <rect x="0" y="12" width="6" height="8"/><rect x="8" y="9" width="6" height="11"/>
    <rect x="16" y="6" width="6" height="14"/><rect x="24" y="3" width="6" height="17"/>
    <rect x="32" y="0" width="6" height="20"/>
  </svg>
  <span class="carrier">NorthTel</span>
  <span class="clock">10:20 PM</span>
  <svg class="alarm" width="26" height="26" viewBox="0 0 26 26">
    <circle cx="13" cy="13" r="12" fill="#fff"/>
    <path d="M13 6 V13 H18" stroke="#000" stroke-width="3" fill="none"/>
  </svg>
  <svg class="battery" width="52" height="24" viewBox="0 0 52 24">
    <rect x="1.5" y="1.5" width="44" height="21" rx="3" fill="none" stroke="#fff" stroke-width="3"/>
    <rect x="6" y="6" width="35" height="12" fill="#fff"/>
    <rect x="47" y="8" width="4" height="8" fill="#fff"/>
  </svg>
</header>

<nav class="nav-bar">
  <h1 class="nav-title">Home</h1>
  <div class="sign-out">Sign Out</div>
</nav>

<div class="search-band">
  <div class="search-field">
    <svg width="34" height="36" viewBox="0 0 34 36">
      <circle cx="14" cy="14" r="11" fill="none" stroke="#8a8a8a" stroke-width="5"/>
      <path d="M22 23 L31 33" stroke="#8a8a8a" stroke-width="6" stroke-linecap="round"/>
    </svg>
    <span class="placeholder">Search</span>
  </div>
</div>

<main class="home-grid">
  <div class="divider vertical"></div>
  <div class="divider row-one"></div>
  <div class="divider row-two"></div>

  <!-- Promotions -->
  <svg class="tile-icon" style="left:127px;top:27px" width="90" height="122" viewBox="0 0 72 98" fill="#fff">
    <path d="M18 42 L26 10 C28 -2 44 0 41 14 L37 38 L62 38 C71 38 72 47 66 51 C72 53 72 61 66 63 C72 66 70 73 64 75 C70 78 67 88 59 88 L30 92 C12 94 0 86 0 72 L2 56 C4 48 10 45 18 42 Z"/>
  </svg>
  <div class="tile-label col-left" style="top:163px">Promotions</div>

  <!-- Catalogue -->
  <svg class="tile-icon" style="left:365px;top:27px" width="150" height="122" viewBox="0 0 120 98">
    <rect x="22" y="2" width="96" height="96" rx="6" fill="#e6f9ff"/>
    <rect x="14" y="0" width="96" height="96" rx="6" fill="#fff"/>
    <g stroke="#fff" stroke-width="5" stroke-linecap="round" fill="none">
      <path d="M4 20 H18"/><path d="M4 36 H18"/><path d="M4 52 H18"/><path d="M4 68 H18"/><path d="M4 84 H18"/>
    </g>
    <g stroke="#47d0f3" stroke-width="2" fill="none">
      <path d="M12 17 V23"/><path d="M12 33 V39"/><path d="M12 49 V55"/><path d="M12 65 V71"/><path d="M12 81 V87"/>
    </g>
  </svg>
  <div class="tile-label col-right" style="top:163px">Catalogue</div>

  <!-- Basket -->
  <svg class="tile-icon" style="left:96px;top:250px" width="150" height="125" viewBox="0 0 120 100">
    <circle cx="60" cy="28" r="27" fill="#fff"/>
    <circle cx="60" cy="28" r="20" fill="#47d0f3"/>
    <path d="M0 32 H34 A27 27 0 0 0 86 32 H120 V72 H0 Z" fill="#fff"/>
    <path d="M0 78 H120 V90 A10 10 0 0 1 110 100 H10 A10 10 0 0 1 0 90 Z" fill="#fff"/>
  </svg>
  <div class="tile-label col-left" style="top:386px">Basket</div>

  <!-- Order Template -->
  <svg class="tile-icon" style="left:394px;top:248px" width="100" height="126" viewBox="0 0 80 101">
    <path d="M0 18 L22 10 L36 92 L14 100 Z" fill="#eafaff"/>
    <path d="M18 0 H64 L80 16 V96 H18 Z" fill="#fff"/>
    <path d="M64 0 V16 H80 Z" fill="#c9f0fb"/>
    <g fill="#47d0f3">
      <rect x="30" y="36" width="38" height="5"/><rect x="30" y="48" width="38" height="5"/>
      <rect x="30" y="60" width="38" height="5"/><rect x="56" y="78" width="12" height="5"/>
    </g>
  </svg>
  <div class="tile-label col-right" style="top:386px">Order Template</div>

  <!-- Open Order -->
  <svg class="tile-icon" style="left:127px;top:463px" width="90" height="124" viewBox="0 0 72 99">
    <path d="M0 0 H54 L72 18 V99 H0 Z" fill="#fff"/>
    <path d="M54 0 V18 H72 Z" fill="#c9f0fb"/>
    <g fill="#47d0f3">
      <rect x="10" y="34" width="52" height="6"/><rect x="10" y="47" width="52" height="6"/>
      <rect x="10" y="60" width="52" height="6"/>
    </g>
    <path d="M40 82 L46 88 L58 76" stroke="#47d0f3" stroke-width="4" fill="none"/>
  </svg>
  <div class="tile-label col-left" style="top:600px">Open Order</div>

  <!-- My Account -->
  <svg class="tile-icon" style="left:369px;top:463px" width="148" height="124" viewBox="0 0 118 99" fill="#fff">
    <ellipse cx="59" cy="32" rx="29" ry="32"/>
    <path d="M0 99 C0 72 22 58 59 58 C96 58 118 72 118 99 Z"/>
  </svg>
  <div class="tile-label col-right" style="top:600px">My Account</div>
</main>

</body>
</html>
```